Tervolan Pty Ltd professional business card

A professional business card template using the colours from the supplied logo.
Clean crisp lines while, Modern while not being over the top.

Target Market(s)

Construction, commerical and industrial

Industry/Entity Type

Communications

Contact Information for Business Card

For a Communications, IT, Optical fibre installation company

Colors
37b8a4

```html
<!DOCTYPE html>
<html lang="en">
<head>
<meta charset="UTF-8">
<title>Tervolan Pty Ltd Business Card</title>
<link href="https://fonts.googleapis.com/css2?family=Montserrat:wght@500;700&family=Arimo:wght@400&display=swap" rel="stylesheet">
<style>
  :root {
    --bg: #e9eaec;
    --card-grey: #6a6b6f;
    --brand-grey: #626366;
    --teal: #1f95a1;
    --white: #ffffff;
  }
  * { margin: 0; padding: 0; box-sizing: border-box; }
  html, body {
    width: 1200px;
    height: 1015px;
    overflow: hidden;
    background: var(--bg);
  }
  .sheet {
    position: relative;
    width: 1200px;
    height: 1015px;
  }
  .card {
    position: absolute;
    left: 220px;
    width: 760px;
    height: 434px;
    overflow: hidden;
    box-shadow: 0 8px 24px rgba(0,0,0,0.18);
  }
  .card--front {
    top: 49px;
    background: var(--card-grey);
    display: flex;
    align-items: center;
    justify-content: center;
  }
  .card--back {
    top: 532px;
    background: var(--card-grey);
  }
  .brand-name {
    font-family: "Montserrat", sans-serif;
    font-weight: 500;
    letter-spacing: 4px;
    text-transform: uppercase;
  }
  .card--front .brand-name {
    color: var(--white);
    font-size: 76px;
  }
  .back-shape {
    position: absolute;
    inset: 0;
    width: 760px;
    height: 434px;
  }
  .card--back .brand-name {
    position: absolute;
    right: 50px;
    top: 150px;
    color: var(--brand-grey);
    font-size: 46px;
    letter-spacing: 3px;
  }
  .contact {
    position: absolute;
    left: 50px;
    top: 170px;
    color: var(--white);
    font-family: "Arimo", sans-serif;
    font-size: 19px;
    line-height: 1.25;
  }
  .contact__name {
    font-family: "Montserrat", sans-serif;
    font-weight: 700;
    font-size: 23px;
    letter-spacing: 0.5px;
    text-transform: uppercase;
  }
  .contact__role { margin-bottom: 10px; }
  .contact__list { list-style: none; }
  .contact__list li {
    display: flex;
    align-items: center;
    gap: 8px;
  }
  .contact__list svg { width: 17px; height: 17px; flex: none; }
  .contact__address { margin-top: 14px; }
</style>
</head>
<body>
<main class="sheet">
  <section class="card card--front">
    <span class="brand-name">Tervolan</span>
  </section>

  <section class="card card--back">
    <svg class="back-shape" viewBox="0 0 760 434" aria-hidden="true">
      <path d="M372 0 H760 V434 H640 C470 390 330 250 372 0 Z" fill="var(--white)"/>
      <path d="M372 0 C330 250 470 390 640 434 L600 434 C420 380 330 240 362 0 Z" fill="var(--teal)"/>
      <path d="M362 0 C330 240 420 380 600 434 L592 434 C410 380 322 240 355 0 Z" fill="var(--white)"/>
    </svg>

    <span class="brand-name">Tervolan</span>

    <div class="contact">
      <p class="contact__name">Marcus Hale</p>
      <p class="contact__role">Managing Director</p>
      <ul class="contact__list">
        <li>
          <svg viewBox="0 0 24 24" fill="none" stroke="currentColor" stroke-width="2"><rect x="2" y="2" width="20" height="20" rx="2"/><path d="M8 6l2 3-1.5 1.5a8 8 0 0 0 5 5L15 14l3 2-1 2.5c-6 0-11-5-11-11z"/></svg>
          061-482 905 317
        </li>
        <li>
          <svg viewBox="0 0 24 24" fill="currentColor"><rect x="6" y="2" width="12" height="6"/><rect x="2" y="9" width="20" height="9" rx="1"/><rect x="6" y="15" width="12" height="7" fill="var(--card-grey)" stroke="currentColor" stroke-width="2"/></svg>
          061-482 905 318
        </li>
        <li>
          <svg viewBox="0 0 24 24" fill="none" stroke="currentColor" stroke-width="2"><rect x="2" y="5" width="20" height="14"/><path d="M2 5l10 8 10-8"/></svg>
          info@tervolan.com
        </li>
        <li>
          <svg viewBox="0 0 24 24" fill="none" stroke="currentColor" stroke-width="2"><circle cx="12" cy="12" r="10"/><path d="M2 12h20M12 2c3 3 3 17 0 20M12 2c-3 3-3 17 0 20"/></svg>
          www.tervolan.com
        </li>
      </ul>
      <p class="contact__address">48 Harbour Link Road<br>Brisbane QLD, 4000.</p>
    </div>
  </section>
</main>
</body>
</html>
```